Eye-catching Yellow Page Ad for Attorney's Office

We need a phone book advertisement for our law office. We practice workers' compensation law, and our clientele consists exclusively of individuals who have been injured on the job. The dimensions of the print ad will be 6" W X 4.54" H.

We've had our current ad for several years, and wanted to get a new one that has been designed by a professional. Being that it's an ad for a law firm, it needs to be professional looking, but we're hoping to have something that looks a little more modern and has eye-catching appeal. We like the text that is included in the ad, and we want to make sure our phone number is very visible. No real preference for color scheme.

I've attached a copy of our current ad. All the information included in there is accurate. Our office name is Thornbury & Lisle, PLLC. The ethical rules for attorney advertising require the PLLC to be included in the ad, but it can be smaller than the other text (see our current ad).

Target Market(s)

Our potential clients are injured workers looking for legal representation in their workers' compensation claim.

Industry/Entity Type

Attorney

Font styles to use
Serif
Sans Serif

Requirements
Must have
• Professional, but stands out from the crowd
Nice to have
• Clean modern design
Should not have
• We don't want it to be too crowded or over-worked.

```html
<!DOCTYPE html>
<html lang="en">
<head>
<meta charset="utf-8">
<title>Thornbury &amp; Lisle PLLC – Workers' Compensation Ad</title>
<link rel="stylesheet" href="https://fonts.googleapis.com/css2?family=Roboto+Condensed:wght@400;700&family=Cormorant+Garamond:ital,wght@1,500;1,600&display=swap">
<style>
  :root {
    --brand-blue: #1873e6;
    --ink-black: #050505;
    --paper: #ffffff;
    --text-dark: #111111;
    --wood-dark: #2a1712;
    --wood-mid: #5a3322;
    --brass: #c98a2c;
  }
  * { box-sizing: border-box; margin: 0; padding: 0; }
  html, body { width: 1200px; height: 1000px; overflow: hidden; background: var(--paper); }

  .ad {
    position: absolute; left: 105px; top: 88px;
    width: 997px; height: 830px;
    background: var(--paper);
    box-shadow: 5px 5px 4px rgba(0,0,0,0.45);
    overflow: hidden;
  }

  .masthead {
    position: absolute; left: 0; top: 0; width: 100%; height: 95px;
    background: var(--brand-blue);
    display: flex; align-items: center; justify-content: center;
    font-family: "Roboto Condensed", sans-serif; font-weight: 700; color: var(--paper);
  }
  .firm-name { font-size: 64px; letter-spacing: 0.5px; }
  .firm-suffix { font-size: 36px; margin-left: 16px; margin-top: 16px; }

  .hero-visual {
    position: absolute; left: 0; top: 95px; width: 100%; height: 282px;
    background:
      radial-gradient(ellipse at 38% 45%, rgba(201,138,44,0.55), transparent 45%),
      radial-gradient(ellipse at 80% 60%, rgba(120,70,40,0.55), transparent 40%),
      linear-gradient(180deg, var(--wood-dark), var(--wood-mid) 60%, var(--wood-dark));
  }

  .tagline-band {
    position: absolute; left: 0; top: 377px; width: 100%; height: 87px;
    background: var(--ink-black);
    font-family: "Cormorant Garamond", serif; font-style: italic; font-weight: 600;
    color: var(--paper); font-size: 36px; line-height: 34px;
    text-align: center; padding-top: 6px;
  }
  .accent { color: var(--brand-blue); }

  .promise {
    position: absolute; left: 0; top: 472px; width: 100%;
    font-family: "Cormorant Garamond", serif; font-style: italic; font-weight: 600;
    color: var(--text-dark); font-size: 32px; line-height: 28px; text-align: center;
  }

  .values {
    position: absolute; left: 0; top: 548px; width: 100%;
    display: flex; justify-content: center; gap: 38px;
    font-family: "Cormorant Garamond", serif; font-style: italic; font-weight: 500;
    font-size: 32px; color: var(--text-dark);
  }
  .values li { list-style: none; display: flex; align-items: center; gap: 8px; }
  .values .blue { color: var(--brand-blue); }
  .arrow { width: 22px; height: 18px; flex: none; }

  .services {
    position: absolute; left: 0; top: 595px; width: 480px; height: 235px;
    background: var(--brand-blue); padding: 12px 0 0 32px;
    font-family: "Roboto Condensed", sans-serif;
  }
  .services-title { font-weight: 700; font-size: 29px; color: var(--text-dark); margin-bottom: 6px; }
  .services-list li {
    list-style: none; display: flex; align-items: center; gap: 10px;
    font-size: 26px; line-height: 28px; color: var(--paper);
  }
  .services-list .arrow { fill: var(--text-dark); }

  .contact {
    position: absolute; left: 480px; top: 595px; width: 517px; height: 235px;
    background: var(--ink-black); color: var(--paper);
    font-family: "Roboto Condensed", sans-serif;
  }
  .contact-row { position: absolute; left: 75px; display: flex; align-items: center; gap: 30px; }
  .contact-icon { width: 54px; height: 48px; fill: var(--brand-blue); flex: none; }
  .phone { top: 10px; }
  .area-code { font-size: 28px; }
  .phone-number { font-size: 52px; }
  .address { top: 82px; font-size: 26px; line-height: 28px; }
  .web { top: 162px; font-size: 26px; }
</style>
</head>
<body>
<main class="ad">
  <header class="masthead">
    <span class="firm-name">Thornbury &amp; Lisle</span><span class="firm-suffix">PLLC</span>
  </header>

  <div class="hero-visual" role="img" aria-label="Brass scales of justice and a wooden gavel in front of shelves of law books"></div>

  <div class="tagline-band">
    <span class="accent">Worker's Compensation:</span> Former Assistant Attorneys General<br>Who Know The System
  </div>

  <p class="promise">
    At Thornbury &amp; Lisle, We provide <span class="accent">Personal</span> Attention to our Clients.<br>
    That means your case is handled by an <span class="accent">Attorney.</span> Not an <span class="accent">Assistant.</span>
  </p>

  <ul class="values">
    <li class="blue"><svg class="arrow" viewBox="0 0 22 18"><path d="M0 0 L22 9 L0 18 L5 9 Z" fill="#111"/></svg>PROFESSIONAL</li>
    <li><svg class="arrow" viewBox="0 0 22 18"><path d="M0 0 L22 9 L0 18 L5 9 Z" fill="#1873e6"/></svg>COMMITTED</li>
    <li class="blue"><svg class="arrow" viewBox="0 0 22 18"><path d="M0 0 L22 9 L0 18 L5 9 Z" fill="#111"/></svg>EFFECTIVE</li>
  </ul>

  <section class="services">
    <h2 class="services-title">We Can Help With:</h2>
    <ul class="services-list">
      <li><svg class="arrow" viewBox="0 0 22 18"><path d="M0 0 L22 9 L0 18 L5 9 Z"/></svg>Workplace Injuries or Death</li>
      <li><svg class="arrow" viewBox="0 0 22 18"><path d="M0 0 L22 9 L0 18 L5 9 Z"/></svg>Lost Wages</li>
      <li><svg class="arrow" viewBox="0 0 22 18"><path d="M0 0 L22 9 L0 18 L5 9 Z"/></svg>Medical Expenses and Treatment</li>
      <li><svg class="arrow" viewBox="0 0 22 18"><path d="M0 0 L22 9 L0 18 L5 9 Z"/></svg>Hearing Loss Claims</li>
      <li><svg class="arrow" viewBox="0 0 22 18"><path d="M0 0 L22 9 L0 18 L5 9 Z"/></svg>Disability Awards</li>
      <li><svg class="arrow" viewBox="0 0 22 18"><path d="M0 0 L22 9 L0 18 L5 9 Z"/></svg>Return to Work Issues</li>
    </ul>
  </section>

  <section class="contact">
    <div class="contact-row phone">
      <svg class="contact-icon" viewBox="0 0 54 48">
        <path d="M4 14 Q27 0 50 14 L48 22 L38 20 L37 14 Q27 10 17 14 L16 20 L6 22 Z"/>
        <path d="M14 22 L40 22 L48 44 L6 44 Z"/>
        <circle cx="27" cy="33" r="6" fill="#050505"/>
      </svg>
      <span><span class="area-code">360</span><span class="phone-number">555-0142</span></span>
    </div>
    <div class="contact-row address">
      <svg class="contact-icon" viewBox="0 0 54 60" style="height:60px">
        <path d="M27 2 L52 26 L44 26 L44 58 L10 58 L10 26 L2 26 Z"/>
        <rect x="20" y="34" width="14" height="14" fill="#050505"/>
      </svg>
      <span>245 W. Harbor Suite 410,<br>Bellingham</span>
    </div>
    <div class="contact-row web">
      <svg class="contact-icon" viewBox="0 0 54 54" style="height:54px">
        <g fill="none" stroke="#1873e6" stroke-width="3">
          <circle cx="27" cy="27" r="24"/>
          <ellipse cx="27" cy="27" rx="11" ry="24"/>
          <line x1="27" y1="3" x2="27" y2="51"/>
          <line x1="3" y1="27" x2="51" y2="27"/>
          <path d="M8 15 H46 M8 39 H46"/>
        </g>
      </svg>
      <span>www.thornburylisle.com</span>
    </div>
  </section>
</main>
</body>
</html>
```